Create a new business card

I’m looking to update my business card to make it match the rest of my brand. I will include my current website as well as what my vehicle designs look like, etc..
What my business currently services
Weekly maintenance pool openings / closings
Equipment repair, including pumps, heaters, salt systems, filters, etc.
We install automatic covers and maintain them as well as provide preventative maintenance

I would like to include my name.
Bradley Kessner.
My title
Owner
My email
Brad@wavecrewnx.com
5079164826
Www.wavecrewnx.com

```html
<!DOCTYPE html>
<html lang="en">
<head>
<meta charset="utf-8">
<title>Wave Crew Pool Care — Business Card</title>
<link rel="stylesheet" href="https://fonts.googleapis.com/css2?family=Arimo:wght@400;700&display=swap">
<style>
  :root {
    --bg: #b9b9bb;
    --white: #ffffff;
    --sky: #2aa9e0;
    --ocean: #1d5fae;
    --navy: #17327a;
    --deep: #12245e;
    --orange: #e8682c;
    --grey: #555b66;
  }
  html, body {
    margin: 0;
    width: 1200px;
    height: 876px;
    overflow: hidden;
    background: var(--bg);
    font-family: "Arimo", Arial, sans-serif;
  }
  .canvas {
    position: relative;
    width: 1200px;
    height: 876px;
    display: flex;
    align-items: center;
    justify-content: center;
    gap: 60px;
  }
  .card {
    position: relative;
    width: 525px;
    height: 300px;
    border-radius: 18px;
    overflow: hidden;
    box-shadow: 0 14px 30px rgba(0,0,0,.25);
  }
  .card-front { background: var(--white); }
  .card-bg { position: absolute; inset: 0; width: 100%; height: 100%; }

  .brand {
    position: absolute;
    left: 40px;
    top: 18px;
    width: 136px;
    height: 136px;
    border-radius: 50%;
    background: var(--white);
    display: flex;
    flex-direction: column;
    align-items: center;
    justify-content: center;
    text-align: center;
    color: var(--navy);
    font-weight: 700;
    box-shadow: 0 0 0 4px var(--sky);
  }
  .brand-name { font-size: 19px; line-height: 1.1; }
  .brand-url { font-size: 8px; margin-top: 7px; letter-spacing: .4px; }

  .identity {
    position: absolute;
    right: 32px;
    top: 48px;
    text-align: right;
  }
  .person-name {
    margin: 0;
    font-size: 23px;
    font-weight: 400;
    letter-spacing: 1px;
    color: var(--sky);
    text-transform: uppercase;
  }
  .person-title {
    margin: 6px 0 0;
    font-size: 15px;
    color: var(--grey);
  }

  .contacts {
    position: absolute;
    right: 30px;
    bottom: 24px;
    list-style: none;
    margin: 0;
    padding: 0;
    color: var(--white);
    font-size: 14px;
    text-align: right;
  }
  .contacts li {
    display: flex;
    align-items: center;
    justify-content: flex-end;
    gap: 10px;
    margin-top: 8px;
  }
  .contacts svg { width: 14px; height: 14px; flex: none; }

  .card-back {
    background: radial-gradient(circle at 40% 30%, #2fb3e6 0%, var(--ocean) 50%, var(--deep) 100%);
  }
  .splash {
    position: absolute;
    left: 50%;
    top: 50%;
    width: 230px;
    height: 200px;
    transform: translate(-50%, -50%);
    border-radius: 48% 52% 45% 55% / 52% 46% 54% 48%;
    background: radial-gradient(circle, #ffffff 55%, #cfeefb 100%);
  }
  .back-brand {
    position: absolute;
    left: 50%;
    top: 50%;
    transform: translate(-50%, -50%);
    display: flex;
    flex-direction: column;
    align-items: center;
    text-align: center;
    color: var(--navy);
    font-weight: 700;
  }
  .back-brand .brand-name { font-size: 22px; }
</style>
</head>
<body>
<main class="canvas">

  <section class="card card-front">
    <svg class="card-bg" viewBox="0 0 525 300" preserveAspectRatio="none" aria-hidden="true">
      <defs>
        <linearGradient id="frontBlue" x1="0" y1="0" x2="1" y2="1">
          <stop offset="0" stop-color="#2aa9e0"/>
          <stop offset=".5" stop-color="#1d5fae"/>
          <stop offset="1" stop-color="#12245e"/>
        </linearGradient>
      </defs>
      <path d="M0 60 C40 70 60 170 190 185 C320 200 430 150 525 155 V300 H0 Z" fill="url(#frontBlue)"/>
      <path d="M0 48 C44 58 62 160 190 174 C270 183 320 176 360 168" fill="none" stroke="#e8682c" stroke-width="5"/>
      <path d="M0 60 C40 70 60 170 190 185 C320 200 430 150 525 155" fill="none" stroke="#2aa9e0" stroke-width="7"/>
    </svg>

    <div class="brand">
      <span class="brand-name">Wave Crew<br>Pool Care</span>
      <span class="brand-url">WWW.WAVECREWNX.COM</span>
    </div>

    <div class="identity">
      <h1 class="person-name">Bradley Kessner</h1>
      <p class="person-title">Owner</p>
    </div>

    <ul class="contacts">
      <li>5079164826
        <svg viewBox="0 0 24 24" fill="currentColor" aria-hidden="true"><path d="M6.6 10.8a15 15 0 0 0 6.6 6.6l2.2-2.2a1 1 0 0 1 1-.25 11.4 11.4 0 0 0 3.6.57 1 1 0 0 1 1 1V20a1 1 0 0 1-1 1A17 17 0 0 1 3 4a1 1 0 0 1 1-1h3.5a1 1 0 0 1 1 1c0 1.25.2 2.450.57 3.57a1 1 0 0 1-.25 1z"/></svg>
      </li>
      <li>Brad@wavecrewnx.com
        <svg viewBox="0 0 24 24" fill="currentColor" aria-hidden="true"><path d="M2 5h20v14H2z M4 7v.5l8 5 8-5V7l-8 5z"/></svg>
      </li>
      <li>Www.wavecrewnx.com
        <svg viewBox="0 0 24 24" fill="none" stroke="currentColor" stroke-width="2" aria-hidden="true"><circle cx="12" cy="12" r="9"/><path d="M3 12h18M12 3c3 3 3 15 0 18M12 3c-3 3-3 15 0 18"/></svg>
      </li>
    </ul>
  </section>

  <section class="card card-back">
    <div class="splash" role="img" aria-label="White water splash behind the company name"></div>
    <div class="back-brand">
      <span class="brand-name">Wave Crew<br>Pool Care</span>
      <span class="brand-url">WWW.WAVECREWNX.COM</span>
    </div>
  </section>

</main>
</body>
</html>
```